Holbrook Legal Group
Project: Stationary for law firm
Stationary for law firm - Law
Stationary for law firm
Use standard fonts
TOMAS VERDELL
Principal Attorney
48210 Pellman Avenue, Suite 415 Woodland Hills, California 90812
legaldesk@brivomail.example
HolbrookLegalGroup.example
dmitrivlaw dmitrivlaw
Kindly note this logo is our old logo design. We have a new logo and files were uploaded.
Please see brief and uploaded files.

```html
<!DOCTYPE html>
<html lang="en">
<head>
<meta charset="utf-8">
<title>Holbrook Legal Group — Business Card</title>
<link rel="stylesheet" href="https://fonts.googleapis.com/css2?family=Cinzel:wght@400;600&family=Open+Sans:wght@400;600&display=swap">
<style>
  :root {
    --backdrop: #e6e7ea;
    --card-white: #ffffff;
    --slate: #5c6a86;
    --slate-deep: #4e5b76;
    --arc-grey: #c8ccd4;
    --ink: #3e4a62;
    --ink-soft: #5a6478;
    --on-slate: #ffffff;
  }
  * { margin: 0; padding: 0; box-sizing: border-box; }
  html, body {
    width: 1200px; height: 959px; overflow: hidden;
    background: var(--backdrop);
  }
  .canvas { position: relative; width: 1200px; height: 959px; }
  .card {
    position: absolute; left: 100px; top: 194px;
    width: 1000px; height: 571px;
    background: var(--card-white);
    overflow: hidden;
    box-shadow: 0 6px 24px rgba(40, 48, 64, 0.18);
  }
  .card-shapes { position: absolute; inset: 0; width: 100%; height: 100%; }
  .brand {
    position: absolute; left: 40px; top: 120px; width: 420px;
    text-align: center; color: var(--ink);
    font-family: "Cinzel", serif;
  }
  .brand-mark {
    width: 64px; height: 64px; margin: 0 auto 26px;
    background: var(--ink);
  }
  .brand-name {
    font-size: 34px; font-weight: 400; letter-spacing: 1px; line-height: 1;
  }
  .brand-person {
    margin-top: 12px; font-size: 15px; letter-spacing: 3px; color: var(--ink-soft);
  }
  .brand-role {
    margin-top: 6px; font-size: 15px; letter-spacing: 2px; color: var(--ink-soft);
  }
  .contact {
    position: absolute; right: 44px; top: 70px;
    text-align: right; color: var(--on-slate);
    font-family: "Open Sans", sans-serif;
  }
  .contact-name { font-size: 25px; font-weight: 600; line-height: 1.2; }
  .contact-title { font-size: 22px; font-weight: 400; line-height: 1.2; margin-bottom: 64px; }
  .contact-line {
    font-size: 20px; line-height: 35px;
    display: flex; justify-content: flex-end; align-items: center; gap: 8px;
  }
  .contact-line svg { width: 16px; height: 16px; fill: var(--on-slate); }
  .contact-gap { margin-top: 4px; }
</style>
</head>
<body>
<div class="canvas">
  <div class="card">
    <svg class="card-shapes" viewBox="0 0 1000 571" preserveAspectRatio="none" aria-hidden="true">
      <path d="M390 0 C610 130 600 420 300 571 L1000 571 L1000 0 Z" fill="var(--arc-grey)"/>
      <path d="M430 0 C640 130 630 430 345 571 L1000 571 L1000 0 Z" fill="var(--slate-deep)"/>
      <path d="M450 0 C650 130 645 430 370 571 L1000 571 L1000 0 Z" fill="var(--slate)"/>
    </svg>

    <div class="brand">
      <div class="brand-mark"></div>
      <div class="brand-name">HOLBROOK LEGAL GROUP</div>
      <div class="brand-person">TOMAS VERDELL, PHD</div>
      <div class="brand-role">PRINCIPAL | ATTORNEY AT LAW</div>
    </div>

    <div class="contact">
      <div class="contact-name">Maren Lisle-Hart</div>
      <div class="contact-title">Consultant</div>
      <div class="contact-line">091.12th floor,Plaza</div>
      <div class="contact-line">Harbor Road LKG</div>
      <div class="contact-line contact-gap">012 345 6789
        <svg viewBox="0 0 16 16"><path d="M3 1l3 0 1 4-2 1c1 2 3 4 5 5l1-2 4 1 0 3c0 1-1 2-2 2C7 15 1 9 1 3c0-1 1-2 2-2z"/></svg>
      </div>
      <div class="contact-line">012 345 6789
        <svg viewBox="0 0 16 16"><path d="M3 1h10v5H3zM1 7h14v7H1zM4 9h2v1H4zm3 0h2v1H7zm3 0h2v1h-2z"/></svg>
      </div>
      <div class="contact-line contact-gap">urname@mailbox.example
        <svg viewBox="0 0 16 16"><path d="M1 3h14v10H1zM2 4l6 5 6-5v-.5H2z" fill-rule="evenodd"/></svg>
      </div>
      <div class="contact-line">www.yourwebsitename.example</div>
    </div>
  </div>
</div>
</body>
</html>
```